Psychotherapeutische Praxis sucht Design und Logo
Zielgruppe
Wir sind approbierte Psychotherapeuten mit mehrjähriger Berufserfahrung und diversen Weiterbildungen.
Wir bieten an: Psychotherapie, Verhaltenstherapie, Supervision, Beratung, Paar- und Familientherapie, Klinische Hypnose
Zielgruppe: primär Kassen- und Privatpatienten, aber auch Psychotherapeutische Supervision für Einzelne und Teams, aber auch klassisches Beratungsklientel und Führungskräfte + Organisationsberatung
Aufgabenstellung
Wir sind eine Praxisgemeinschaft mit derzeit 2 Therapeut(inn)en, es könnte noch ein(e) Dritte(r) dazu kommen.
Es geht darum ein Logo und Design zu entwickeln, das auf den Visitenkarten, auf einem Terminzettel, auf dem Briefbogen und als Header auf unserer neu zu gestaltenden Homepage dient. Weiterhin sollte sich das Thema auch dezent auf einem Praxisschild integrieren lassen.
Es sollte Offenheit, Vertrautheit, Kompetenz und Verständnis signalisiert werden. Und natürlich Hilfe bei seelischen Problemen!
Gerne mit einem freundlichen Grün und einem nicht zu grellen Orange, abgerundet mit Grau, Schwarz oder Weiss - aber auch andere warme Farben sind denkbar - insgesamt nicht mehr als drei.
Ich könnte mir auch vorstellen, dass das Logo im Hintergrund das Zeichen für Psychologie (Psi) und/oder PP für "Psychotherapeutische Praxis" bzw. "Psychologischer Psychotherapeut" beinhaltet - das muss aber nicht sein.
Das Zusammenfügen von etwas das zusammen gehört wäre auch als Thema denkbar. Die (Wieder-)Herstellung einer inneren Harmonie und Ganzheit.
Hintergrund der Neugestaltung ist der geplante Umzug der Praxis in ein anderes Bundesland. Damit verbunden soll auch eine neue Homepage entwickelt werden, diesmal mit Jimdo.

```html
<!DOCTYPE html>
<html lang="de">
<head>
<meta charset="utf-8">
<title>Praxis Lindenau – Geschäftsausstattung</title>
<link href="https://fonts.googleapis.com/css2?family=Open+Sans:wght@300;400;600&display=swap" rel="stylesheet">
<style>
  :root {
    --bg: #4b4c4c;
    --paper: #ffffff;
    --sidebar: #3e3f3f;
    --green: #97c11f;
    --ink: #333434;
    --ink-soft: #8a8b8b;
    --rule: #6a6b6b;
  }
  * { box-sizing: border-box; margin: 0; padding: 0; }
  html, body { width: 1200px; height: 900px; overflow: hidden; }
  body {
    background: var(--bg);
    font-family: "Open Sans", sans-serif;
    color: var(--ink);
    position: relative;
  }

  /* Letterhead */
  .letterhead {
    position: absolute; left: 110px; top: 130px;
    width: 440px; height: 622px;
    background: var(--paper);
    box-shadow: 0 10px 30px rgba(0,0,0,.35);
  }
  .letterhead__sender {
    position: absolute; left: 36px; top: 150px;
    font-size: 7px; font-weight: 600; letter-spacing: .2px;
  }
  .letterhead__sidebar {
    position: absolute; right: 22px; top: 0;
    width: 132px; height: 570px;
    background: var(--sidebar);
    border-radius: 0 0 10px 10px;
    color: #fff;
    padding: 34px 14px 0;
  }
  .letterhead__tail {
    position: absolute; left: 10px; bottom: -12px;
  }
  .brand-mark {
    display: flex; align-items: center; gap: 6px;
    font-weight: 300; font-size: 13px;
  }
  .brand-mark__square {
    width: 14px; height: 14px; background: var(--green); flex: none;
  }
  .letterhead__sidebar .brand-mark { color: #fff; font-size: 12px; }
  .contact { margin-top: 36px; font-size: 8.5px; line-height: 1.45; }
  .contact__mail { color: var(--green); }
  .contact__rule { border: 0; border-top: 1px solid var(--rule); margin: 14px 0 60px; }
  .services { list-style: none; font-size: 9.5px; line-height: 1.6; }
  .services li::before { content: "•"; color: var(--green); margin-right: 5px; }
  .letterhead__url {
    position: absolute; left: 14px; bottom: 16px;
    font-size: 9px; color: var(--green);
  }

  /* Business card */
  .business-card {
    position: absolute; left: 620px; top: 130px;
    width: 340px; height: 200px;
    background: var(--paper);
    box-shadow: 0 10px 26px rgba(0,0,0,.35);
    padding: 34px 30px;
  }
  .business-card__name { font-size: 20px; font-weight: 300; color: var(--ink); }
  .business-card__person { margin-top: 14px; font-size: 8px; font-weight: 600; }
  .business-card__roles { list-style: none; margin-top: 10px; font-size: 7.5px; line-height: 1.6; }
  .business-card__roles li::before { content: "• "; }
  .business-card__divider {
    position: absolute; left: 196px; top: 96px;
    width: 2px; height: 46px; background: var(--green);
  }
  .business-card__square {
    position: absolute; right: 30px; top: 34px;
    width: 26px; height: 26px; background: var(--green);
  }
  .business-card__contact {
    position: absolute; left: 212px; top: 96px;
    font-size: 7.5px; line-height: 1.7;
  }
  .business-card__contact .accent { color: var(--green); }

  /* Compliment card */
  .compliment-card {
    position: absolute; left: 620px; top: 420px;
    width: 470px; height: 250px;
    background: var(--paper);
    box-shadow: 0 10px 30px rgba(0,0,0,.35);
  }
  .compliment-card__square {
    position: absolute; right: 50px; top: 60px;
    width: 40px; height: 40px; background: var(--green);
  }
  .compliment-card__name {
    position: absolute; right: 50px; top: 118px;
    font-size: 30px; font-weight: 300; color: var(--ink);
  }
  .compliment-card__band {
    position: absolute; left: 0; bottom: 0;
    width: 310px; height: 12px; background: var(--green);
  }
</style>
</head>
<body>

  <section class="letterhead">
    <p class="letterhead__sender">Praxis für Psychotherapie • Dr. phil. Dipl.-Psych. Matthias Berkenfeld • Lindenweg 12 • 01234 Musterstadt</p>
    <aside class="letterhead__sidebar">
      <div class="brand-mark"><span class="brand-mark__square"></span>praxislindenau</div>
      <div class="contact">
        <p>Dr. Matthias Berkenfeld:</p>
        <p class="contact__mail">kontakt@praxis-lindenau.de</p>
        <p>Tel.: +49 (0) 123 - 456 78 90</p>
      </div>
      <hr class="contact__rule">
      <ul class="services">
        <li>Psychotherapie</li>
        <li>Verhaltenstherapie</li>
        <li>Supervision</li>
        <li>Beratung</li>
        <li>Klinische Hypnose</li>
      </ul>
      <p class="letterhead__url">www.praxis-lindenau.de</p>
      <svg class="letterhead__tail" width="14" height="12" viewBox="0 0 14 12" aria-hidden="true">
        <path d="M0 0 H14 L2 12 Z" fill="#3e3f3f"/>
      </svg>
    </aside>
  </section>

  <section class="business-card">
    <h1 class="business-card__name">praxislindenau</h1>
    <p class="business-card__person">Dr. Matthias Berkenfeld:</p>
    <ul class="business-card__roles">
      <li>Diplom-Psychologe</li>
      <li>Psychologischer Psychotherapeut</li>
    </ul>
    <span class="business-card__square"></span>
    <span class="business-card__divider"></span>
    <div class="business-card__contact">
      <p>kontakt@praxis-lindenau.de</p>
      <p>Tel.: <span class="accent">+49 (0) 123 - 456 78 90</span></p>
      <p class="accent">www.praxis-lindenau.de</p>
    </div>
  </section>

  <section class="compliment-card">
    <span class="compliment-card__square"></span>
    <p class="compliment-card__name">praxis-lindenau.de</p>
    <span class="compliment-card__band"></span>
  </section>

</body>
</html>
```